Corporate marketing website with signup form

The function of the website is to promote our 2 product offerings. It will contain a main screen and several 5-7 sub-pages that will be available as 'scroll down' anchors and as front-page navigation links on the top of the page.

Navigation menu labels are: Products, Unique Model, Pricing, About, and Contact

Target Market(s)

Business to business marketers who are looking to source lead generation services

Industry/Entity Type

Marketing

Logo Text

Velmora

Coding

Coded - Design and coding required

Number of Pages Required

5+ page

Requirements
Must have
• A sign-up form on main section of the front page. Fields are First Name, Last Name, Company, and Email (all text), and a pull-down with three options (only pick one): Track 1, Track 2, Custom Combination.
• Also incorporate the bottom half (ie crop the image) of the EPS file attached (the 'blue heads). Add this to the lower portion of the main screen and have the rest of the blue background become the background for the next anchored section of the navigation.
• You'll see the main section text in the mock-up I provided. The rest of the menu items/anchors can be lorem ipsum for now.
• Can this be coded in Wordpress? That would be my preference so I can edit it in the future.

```html
<!DOCTYPE html>
<html lang="en">
<head>
<meta charset="utf-8">
<title>Velmora — List and Audience Building</title>
<link rel="stylesheet" href="https://fonts.googleapis.com/css2?family=Arimo:ital,wght@0,400;0,700;1,700&family=PT+Sans:ital,wght@0,400;0,700;1,400&display=swap">
<style>
  :root {
    --sky: #70c9e5;
    --white: #ffffff;
    --navy: #0f2a44;
    --ink: #222222;
    --grey-text: #555555;
    --field-border: #b5b5b5;
    --field-text: #9a9a9a;
    --btn-dark: #555555;
    --social-a: #3a5798;
    --social-b: #1aa3e0;
    --rule: #3a5798;
    --band: #6cc4e1;
  }
  * { box-sizing: border-box; margin: 0; padding: 0; }
  html, body { width: 1041px; height: 1200px; overflow: hidden; }
  body { position: relative; background: var(--white); font-family: "Arimo", Arial, sans-serif; }

  /* Header */
  .site-header { position: absolute; left: 0; top: 0; width: 1041px; height: 66px; background: var(--white); }
  .brand { position: absolute; left: 154px; top: 15px; font-size: 30px; color: var(--navy); font-weight: 400; }
  .main-nav a { position: absolute; top: 22px; height: 27px; line-height: 27px; font-size: 14px; color: var(--ink); text-decoration: none; transform: translateX(-50%); white-space: nowrap; }
  .main-nav .is-active { background: var(--sky); color: var(--white); border-radius: 14px; padding: 0 17px; }

  /* Hero */
  .hero { position: absolute; left: 0; top: 66px; width: 1041px; height: 504px; background: var(--sky); }
  .hero-title { position: absolute; left: 154px; top: 122px; width: 380px; font-size: 25px; line-height: 30px; font-weight: 700; color: var(--white); }
  .hero-lead { position: absolute; left: 154px; top: 197px; width: 360px; font-size: 13.5px; line-height: 16px; font-weight: 700; font-style: italic; color: var(--white); }
  .hero-note { position: absolute; left: 154px; top: 260px; font-size: 12px; color: var(--white); }

  .signup-card { position: absolute; left: 556px; top: 32px; width: 330px; height: 417px; background: var(--white); border-radius: 3px; font-family: "PT Sans", Arial, sans-serif; box-shadow: 0 12px 10px -8px rgba(0,0,0,.55), 0 20px 60px rgba(255,255,255,.25); }
  .card-title { position: absolute; left: 0; width: 100%; text-align: center; font-size: 21px; font-weight: 700; color: #333; }
  .social { position: absolute; left: 38px; top: 64px; width: 253px; height: 42px; border-radius: 7px; overflow: hidden; display: flex; }
  .social span { display: block; height: 100%; line-height: 42px; color: var(--white); font-size: 19px; font-weight: 700; text-align: center; }
  .social .name-a { width: 128px; background: var(--social-a); }
  .social .name-b { width: 125px; background: var(--social-b); }
  .divider { position: absolute; left: 46px; top: 143px; width: 238px; height: 1px; }
  .divider::before, .divider::after { content: ""; position: absolute; top: 0; width: 99px; height: 1px; background: var(--rule); }
  .divider::before { left: 0; } .divider::after { right: 0; }
  .divider span { position: absolute; left: 50%; top: -11px; transform: translateX(-50%); font-style: italic; font-size: 16px; color: var(--rule); }
  .field { position: absolute; height: 26px; border: 1px solid var(--field-border); border-radius: 3px; font-size: 11.5px; color: var(--field-text); line-height: 24px; padding-left: 7px; }
  .field.select::after { content: ""; position: absolute; right: 0; top: 0; width: 26px; height: 24px; border-left: 1px solid var(--field-border); }
  .field.select i { position: absolute; right: 8px; top: 9px; width: 0; height: 0; border-left: 4px solid transparent; border-right: 4px solid transparent; border-top: 6px solid #777; }
  .btn-signup { position: absolute; left: 108px; top: 340px; width: 115px; height: 32px; background: var(--btn-dark); color: var(--white); border-radius: 3px; text-align: center; line-height: 32px; font-size: 16px; font-weight: 700; }
  .member { position: absolute; left: 0; top: 387px; width: 100%; text-align: center; font-size: 7.5px; color: #333; }
  .member b { margin-left: 6px; }

  /* Tracks */
  .tracks { position: absolute; left: 0; top: 570px; width: 1041px; height: 582px; }
  .tracks svg { position: absolute; left: 0; top: 0; }
  .track-title { position: absolute; font-size: 35px; font-weight: 400; }
  .track-one { color: var(--grey-text); }
  .track-two { color: var(--white); }
  .t-sub { position: absolute; font-size: 13px; font-weight: 700; }
  .t-text { position: absolute; font-size: 12px; line-height: 18px; }
  .t-small { position: absolute; font-size: 11.5px; line-height: 14.4px; color: var(--white); }

  /* Footer */
  .site-footer { position: absolute; left: 0; top: 1152px; width: 1041px; height: 48px; background: var(--white); font-family: "PT Sans", Arial, sans-serif; }
  .footer-band { position: absolute; left: 0; width: 100%; height: 6px; background: var(--band); }
  .footer-band.top { top: 1px; } .footer-band.bottom { top: 41px; }
  .copyright { position: absolute; left: 0; top: 15px; width: 100%; text-align: center; font-size: 11.5px; color: #666; letter-spacing: .3px; }
</style>
</head>
<body>
  <header class="site-header">
    <div class="brand">Velmora</div>
    <nav class="main-nav">
      <a class="is-active" style="left:475px">Products</a>
      <a style="left:582px">Unique Model</a>
      <a style="left:680px">Pricing</a>
      <a style="left:754px">About</a>
      <a style="left:829px">Contact</a>
    </nav>
  </header>

  <section class="hero">
    <h1 class="hero-title">List and Audience Building for your Content Marketing Efforts</h1>
    <p class="hero-lead">Lorem Ipsum is simply dummy text of the printing and typesetting industry. Lorem Ipsum has been the indus-try's standard dummy text</p>
    <p class="hero-note">Give us your ideal target title, COMPANY Size and Industry</p>

    <form class="signup-card">
      <div class="card-title" style="top:14px">Sign up with</div>
      <div class="social">
        <span class="name-a">Friendnet</span><span class="name-b">Chirpline</span>
      </div>
      <div class="divider"><span>or</span></div>
      <div class="card-title" style="top:157px">Create an account</div>
      <div class="field" style="left:17px;top:209px;width:140px">First Name</div>
      <div class="field" style="left:174px;top:209px;width:132px">Last Name</div>
      <div class="field" style="left:17px;top:249px;width:140px">Company</div>
      <div class="field select" style="left:174px;top:249px;width:132px">Select<i></i></div>
      <div class="field" style="left:17px;top:290px;width:289px">Email</div>
      <div class="btn-signup">Sign Up</div>
      <div class="member">Already a member? <b>Login here</b></div>
    </form>
  </section>

  <section class="tracks">
    <svg width="1041" height="582" viewBox="0 0 1041 582">
      <polygon fill="#70c9e5" points="0,0 97,0 319,70 319,150 598,308 886,398 886,474 1041,560 1041,582 0,582"/>
      <line x1="350" y1="91" x2="886" y2="91" stroke="#70c9e5" stroke-width="1"/>
      <circle cx="350" cy="91" r="8.5" fill="#70c9e5"/>
      <line x1="162" y1="324" x2="637" y2="324" stroke="#ffffff" stroke-width="1"/>
      <circle cx="162" cy="324" r="8.5" fill="#ffffff"/>
    </svg>

    <h2 class="track-title track-one" style="left:393px;top:50px">Track1</h2>
    <p class="t-sub" style="left:454px;top:109px;color:var(--grey-text)">Update, enhance or adppend you existing prospect database</p>
    <p class="t-text" style="left:478px;top:141px;color:var(--grey-text)">Give us your ideal target title, COMPANY Size and Industry</p>
    <p class="t-text" style="left:503px;top:169px;width:360px;color:var(--grey-text)">We provide contact lists derived from real-time data for your target including emails and phone numbers<br>Coming soon: Discover what services and technologies are being evaluated or used within your lists</p>

    <h2 class="track-title track-two" style="left:200px;top:284px">Track2</h2>
    <p class="t-sub" style="left:207px;top:352px;width:380px;line-height:16px;color:var(--white)">Lorem ipsum dolor sit amet, consectetuer adipiscing elit,<br>sed diam nonummy nibh euismod tincidunt ut laoreet<br>dolore magna aliquam erat volutpat. Ut wisi enim ad minim</p>
    <p class="t-small" style="left:280px;top:414px;width:400px">Lorem ipsum dolor sit amet, consectetuer adipiscing elit, sed diam<br>nonummy nibh euismod tincidunt ut laoreet dolore magna aliquam erat<br>volutpat. Ut wisi enim ad minim veniam, quis nostrud exerci tation ullam-</p>
    <p class="t-small" style="left:380px;top:477px;width:340px">Lorem ipsum dolor sit amet, consectetuer adipiscing elit, sed<br>diam nonummy nibh euismod tincidunt ut laoreet dolore<br>magna aliquam erat volutpat. Ut wisi enim ad minim veniam,</p>
  </section>

  <footer class="site-footer">
    <div class="footer-band top" role="img" aria-label="Decorative footer border"></div>
    <p class="copyright">Copyright © 2016 . All rights reserved.</p>
    <div class="footer-band bottom" role="img" aria-label="Decorative footer border"></div>
  </footer>
</body>
</html>
```